Stationery Design Project - Tax Professionals/(plain badge, no letters)

The name of our firm is “Pellow Group” and our slogan is “Strategic Solutions”. You can also use the name "The Pellow Group" if it works better.

We are looking for a full stationery design: Letterhead, Business Card and With Compliments slip

We are looking for a bold, modern and clean/simple design that makes us stand out. We stand out as professionals in the industry and would like the stationery that our clients see to convey this image as well.

There is no colour preference.

We have used a "Lion" as our logo/symbol and that has received positive feedback from our clients; if you think the lion works then please incorporate the "lion".

If you think another symbol works then please submit this we are very open to ideas and would like to see designs that don't incorporate a lion as well.

We would like a corporate feel to this.

You could also incorporate the LG logo http://www.ledgerguildexample.com.au/Members/Marketing-your-practice/Logos but this is not a must.

WHO WE ARE:-
We are a Chartered Accounting firm who specialise in the delivery of taxation and strategic insolvency services. We also provide financial reporting services that help clients negotiate and compromise their debt or expenses such as rent with their landlords.

We work with Law Firms, other Accountants to deliver the best service for our clients.

Our clients come from varied backgrounds and are largely successful and established businesses and high net worth individuals looks for effective tax planning.

We are not the usual accounting firm and do not provide traditional tax return based services.
Updates

Target Market(s)

Corporate/ Independent successful businesses and individuals

Industry/Entity Type

Business

Requirements
Must have
• The letter must have the following phrase
“Liability limited by a scheme approved under Professional Standards Legislation”

The letter must also have the following business information:-
“The Pellow Group Pty Ltd atf
Principal - Martin K. Pellow
ABN: 47 205 318 664”

Plus Usual Address & Contact Details

We would also a logo or symbol that is representative of us. We like the idea of a lion but this is not set in stone and are very open to ideas.

```html
<!DOCTYPE html>
<html lang="en">
<head>
<meta charset="utf-8">
<title>The Pellow Group – Stationery Set</title>
<link href="https://fonts.googleapis.com/css2?family=Arimo:wght@400;700&display=swap" rel="stylesheet">
<style>
  :root{
    --backdrop:#d8d1c6;
    --paper:#ffffff;
    --ink:#222222;
    --muted:#555555;
    --rule:#333333;
    --hairline:#d6d6d6;
    --red:#c8102e;
    --label:#ffffff;
    --watermark:#ececec;
  }
  *{box-sizing:border-box;margin:0;padding:0}
  html,body{width:1200px;height:527px;overflow:hidden}
  body{background:var(--backdrop);font-family:"Arimo",Arial,sans-serif;color:var(--ink);position:relative}
  .sheet{position:absolute;background:var(--paper);box-shadow:0 1px 3px rgba(0,0,0,.25)}

  /* brand mark */
  .mark{display:flex;align-items:center;gap:.35em;font-size:8px;position:absolute}
  .mark-dot{width:2.4em;height:2.4em;border-radius:50%;background:var(--ink);flex:none}
  .mark-text{display:flex;flex-direction:column;line-height:1.15}
  .mark-name{color:var(--red);font-weight:700;font-size:1em;white-space:nowrap}
  .mark-tagline{color:var(--muted);font-size:.8em;white-space:nowrap}

  .small{font-size:5px;color:var(--muted);line-height:1.55}
  .contact-line{display:flex;align-items:center;gap:3px;white-space:nowrap}
  .icon{width:5px;height:5px;flex:none}

  /* letterhead */
  .letterhead{left:40px;top:18px;width:314px;height:408px}
  .letterhead .business-info{position:absolute;right:12px;top:8px;font-size:5.5px;color:var(--muted);line-height:1.5}
  .letterhead .watermark{position:absolute;left:0;right:0;top:230px;text-align:center;font-weight:700;font-size:22px;color:var(--watermark);transform:rotate(-8deg)}
  .letterhead .liability{position:absolute;left:0;right:0;top:374px;text-align:center;font-size:5.5px;color:var(--muted)}
  .letterhead .footer-rule{position:absolute;left:20px;right:20px;top:383px;border-top:1px solid var(--hairline)}
  .letterhead .address{position:absolute;left:0;right:0;top:388px;text-align:center;font-size:5.5px;color:var(--muted)}
  .letterhead .contacts{position:absolute;left:36px;right:36px;top:397px;display:flex;justify-content:space-between;font-size:5.5px;color:var(--muted)}

  /* fax */
  .fax{left:376px;top:18px;width:314px;height:408px}
  .fax .mark{left:84px;top:16px}
  .fax .contact-block{position:absolute;left:180px;top:12px;padding-left:5px;border-left:1px solid var(--hairline)}
  .fax-title{position:absolute;left:24px;top:94px;font-size:20px;font-weight:400}
  .fax-fields{position:absolute;left:22px;top:128px;width:270px;display:grid;grid-template-columns:1fr 1fr;column-gap:20px;row-gap:7px}
  .fax-field{font-size:5.5px;color:var(--muted);border-bottom:1px solid var(--rule);padding-bottom:2px;height:10px}
  .fax-options{position:absolute;left:22px;top:206px;width:270px;display:flex;justify-content:space-between;font-size:5.5px;color:var(--muted)}
  .fax-option{display:flex;align-items:center;gap:3px}
  .checkbox{width:7px;height:7px;border:1px solid var(--rule)}

  /* envelopes */
  .envelope svg{position:absolute;inset:0}
  .envelope-back-1{left:795px;top:43px;width:375px;height:220px}
  .envelope-back-2{left:716px;top:110px;width:382px;height:190px}
  .envelope-back-1 .mark{left:150px;top:12px}
  .envelope-back-2 .mark{left:152px;top:10px}
  .envelope-front{left:754px;top:181px;width:353px;height:159px}
  .envelope-front .mark{left:18px;top:14px}
  .envelope-front .address{position:absolute;left:11px;top:74px;width:80px}
  .envelope-front .rule{position:absolute;left:8px;right:12px;top:143px;border-top:1px solid var(--hairline)}
  .envelope-front .web{position:absolute;left:11px;top:147px}

  /* compliments slip */
  .compliments{left:543px;top:438px;width:147px;height:55px}
  .compliments .mark{left:8px;top:12px;font-size:5px}
  .compliments .details{position:absolute;left:84px;top:5px;font-size:3.4px}
  .compliments .person{font-size:4.5px;color:var(--red);font-weight:700}

  /* business cards */
  .bc-front{left:740px;top:365px;width:195px;height:111px}
  .bc-front .mark{left:10px;top:32px;font-size:7px}
  .bc-front .details{position:absolute;left:110px;top:16px}
  .person-name{font-size:7px;color:var(--red);font-weight:700;margin-bottom:3px}
  .person-name span{font-weight:400;font-size:5px}
  .badge{width:14px;height:14px;border-radius:50%;background:var(--red);margin-top:5px}
  .bc-back{left:965px;top:365px;width:195px;height:111px}
  .bc-back .mark{left:50px;top:24px;font-size:8px}
  .bc-back .web{position:absolute;left:0;right:0;top:93px;text-align:center;font-size:7px;color:var(--red)}

  .caption{position:absolute;font-size:11px;color:var(--label);text-shadow:0 0 2px rgba(0,0,0,.4)}
</style>
</head>
<body>

<svg width="0" height="0" style="position:absolute">
  <defs>
    <symbol id="icon-phone" viewBox="0 0 10 10"><path d="M2 1l2 2-1 1.5c.8 1.4 1.7 2.3 3 3L7.5 6l2 2-1.5 1.5C4.5 9 1 5.5.5 2.5z" fill="#555"/></symbol>
    <symbol id="icon-mobile" viewBox="0 0 10 10"><rect x="3" y="0.5" width="4" height="9" rx="0.8" fill="#555"/></symbol>
    <symbol id="icon-mail" viewBox="0 0 10 10"><rect x="0.5" y="2" width="9" height="6" fill="#555"/><path d="M.5 2L5 5.5 9.5 2" stroke="#fff" fill="none"/></symbol>
    <symbol id="icon-web" viewBox="0 0 10 10"><circle cx="5" cy="5" r="4.2" fill="none" stroke="#555"/><path d="M1 5h8M5 1v8" stroke="#555"/></symbol>
  </defs>
</svg>

<!-- Letterhead -->
<section class="sheet letterhead">
  <div class="business-info">Principal - Martin K. Pellow<br>ABN: 47 205 318 664</div>
  <div class="watermark">The Pellow Group Pty Ltd atf</div>
  <p class="liability">Liability limited by a scheme approved under Professional Standards Legislation</p>
  <div class="footer-rule"></div>
  <p class="address">Complex Name, Street Name, Area, City Name:000 000</p>
  <div class="contacts">
    <span class="contact-line"><svg class="icon"><use href="#icon-phone"/></svg>+91 55501 24680</span>
    <span class="contact-line"><svg class="icon"><use href="#icon-mobile"/></svg>+91 55501 24680</span>
    <span class="contact-line"><svg class="icon"><use href="#icon-mail"/></svg>pellowgroup@samplemail.in</span>
    <span class="contact-line"><svg class="icon"><use href="#icon-web"/></svg>www.pellowgroup.com</span>
  </div>
</section>

<!-- Fax cover -->
<section class="sheet fax">
  <div class="mark"><span class="mark-dot"></span><span class="mark-text"><span class="mark-name">The Pellow Group</span><span class="mark-tagline">Strategic Solutions</span></span></div>
  <div class="contact-block small">
    <div class="contact-line"><svg class="icon"><use href="#icon-phone"/></svg>+91 55501 24680</div>
    <div class="contact-line"><svg class="icon"><use href="#icon-mobile"/></svg>+91 55501 24680</div>
    <div class="contact-line"><svg class="icon"><use href="#icon-mail"/></svg>pellowgroup@samplemail.in</div>
    <div class="contact-line"><svg class="icon"><use href="#icon-web"/></svg>www.pellowgroup.com</div>
    <div>Complex Name, Street Name,<br>Area, City Name:000 000</div>
  </div>
  <h1 class="fax-title">FAX</h1>
  <div class="fax-fields">
    <div class="fax-field">To :</div><div class="fax-field">From :</div>
    <div class="fax-field">Fax :</div><div class="fax-field">Pages :</div>
    <div class="fax-field">Phone :</div><div class="fax-field">Date :</div>
    <div class="fax-field">Re :</div><div class="fax-field">CC :</div>
  </div>
  <div class="fax-options">
    <span class="fax-option"><span class="checkbox"></span>Urgent</span>
    <span class="fax-option"><span class="checkbox"></span>For Review</span>
    <span class="fax-option"><span class="checkbox"></span>Please Comment</span>
    <span class="fax-option"><span class="checkbox"></span>Please Reply</span>
    <span class="fax-option"><span class="checkbox"></span>Please Recycle</span>
  </div>
</section>

<!-- Envelopes -->
<section class="sheet envelope envelope-back-1">
  <svg width="375" height="220"><polyline points="0,0 187,46 375,0" fill="none" stroke="#cfcfcf"/></svg>
  <div class="mark"><span class="mark-dot"></span><span class="mark-text"><span class="mark-name">The Pellow Group</span><span class="mark-tagline">Strategic Solutions</span></span></div>
</section>
<section class="sheet envelope envelope-back-2">
  <svg width="382" height="190"><polyline points="0,0 191,50 382,0" fill="none" stroke="#cfcfcf"/></svg>
  <div class="mark"><span class="mark-dot"></span><span class="mark-text"><span class="mark-name">The Pellow Group</span><span class="mark-tagline">Strategic Solutions</span></span></div>
</section>
<section class="sheet envelope envelope-front">
  <div class="mark"><span class="mark-dot"></span><span class="mark-text"><span class="mark-name">The Pellow Group</span><span class="mark-tagline">Strategic Solutions</span></span></div>
  <p class="address small">Complex Name, Street Name, Area, City Name:000 000</p>
  <div class="rule"></div>
  <p class="web small">www.pellowgroup.com</p>
</section>

<!-- Compliments slip -->
<section class="sheet compliments">
  <div class="mark"><span class="mark-dot"></span><span class="mark-text"><span class="mark-name">The Pellow Group</span><span class="mark-tagline">Strategic Solutions</span></span></div>
  <div class="details small">
    <div class="person">Name Here / <span style="font-weight:400">Title</span></div>
    <div>+91 55501 24680</div>
    <div>+91 55501 24680</div>
    <div>pellowgroup@samplemail.in</div>
    <div>www.pellowgroup.com</div>
    <div>Complex Name, Street Name,<br>Area, City Name:000 000</div>
    <div class="badge" style="width:7px;height:7px;margin-top:2px"></div>
  </div>
</section>
<p class="caption" style="left:576px;top:499px">Compliments slip</p>

<!-- Business card front -->
<section class="sheet bc-front">
  <div class="mark"><span class="mark-dot"></span><span class="mark-text"><span class="mark-name">The Pellow Group</span><span class="mark-tagline">Strategic Solutions</span></span></div>
  <div class="details small">
    <div class="person-name">Name Here / <span>Title</span></div>
    <div class="contact-line"><svg class="icon"><use href="#icon-phone"/></svg>+91 55501 24680</div>
    <div class="contact-line"><svg class="icon"><use href="#icon-mobile"/></svg>+91 55501 24680</div>
    <div class="contact-line"><svg class="icon"><use href="#icon-mail"/></svg>pellowgroup@samplemail.in</div>
    <div class="contact-line"><svg class="icon"><use href="#icon-web"/></svg>www.pellowgroup.com</div>
    <div>Complex Name, Street Name,<br>Area, City Name:000 000</div>
    <div class="badge" aria-label="Professional body badge"></div>
  </div>
</section>
<p class="caption" style="left:816px;top:483px">BC Front</p>

<!-- Business card back -->
<section class="sheet bc-back">
  <div class="mark"><span class="mark-dot"></span><span class="mark-text"><span class="mark-name">The Pellow Group</span><span class="mark-tagline">Strategic Solutions</span></span></div>
  <p class="web">www.pellowgroup.com</p>
</section>
<p class="caption" style="left:1042px;top:483px">BC Back</p>

</body>
</html>
```